Energy Supplement Company Needs Packaging Design! See Your Design In Stores Everywhere!

Have you ever dreamed of seeing your designs on store shelves, billboards and in the hands of celebrities and professional athletes?

Well, your dreams may just come true… You now have the chance to have your design on the product packaging of the next major energy supplement company!

BRISKLO Vigor, Inc. is inviting the most creative, ambitious and talented designers to create a new look and feel for our brand's most popular products, the BRISKLO Vigor Tablets.

BRISKLO Vigor, Inc. began in 1985 by creating the original energy tablet, most recognized for its iconic blue packet featured in over 20,000 retail stores today. The company grew through their grass roots philosophy of distribution and quickly expanded across the United States through dozens of regional and national chains like 4-22, Marlow Q and PVD. In February of 2001, the founder of BriskLo passed and the company’s grass roots approach lost momentum and distribution as the fierce competition from energy shots and drinks hit the space that they once owned.

Theodore Lasko, a 26 year user of BRISKLO tablets, noticed that his favorite daily energy product was becoming increasingly more difficult to find in stores. As an active, serial entrepreneur with numerous ventures, his deep passion for BRISKLO led him to explore the opportunity to get involved with the company (get involved is an understatement). On August 1st of 2012, Theo raised capital and bought the company.

To increase awareness and spread his passion for BRISKLO, Mr. Lasko organized and structured the new BRISKLO Vigor, Inc. by bringing on a talented Team and investors, including Rex Palmore, a renowned sports agent/owner of the largest basketball agency whose clients include some of the biggest names in the sport. The amazing quality of our products coupled with the loyal following from the masses has led the brand to new heights and sponsorship opportunities with major sports teams and athletic organizations.

Now that the future is looking UP, we are looking for a brand refresh to bring our tablets current.

Your mission -should you chose to accept- is to develop a new graphic design for our energy tablet packets. We expect the graphic design to be modern, sleek and appealing to an 18-34 demographic. This new design will serve as the vehicle to spark excitement about energy tablets and their superiority over other forms of energy supplements. However, most importantly, you must make the package eye catching yet trusting and approachable. Keep in mind that this is something you would see in a retail store and feel comfortable reaching for and trying.

It is important to stress the mainstream direction of our company. The current packaging is somewhat 'dated' and may be out of touch with mainstream interests. Just like your aunt still rocking shoulder pads and leg warmers, we need to leave the 1980s and join everyone in 2013. Although we will begin positioning our brand towards mainstream sports, our goal is to have our products everywhere from the sidelines of major sporting events to board meetings of fortune 500 companies to the backpacks of college students. Therefore, the winning design will be one that transcends the interests of a specific group and appeals to the broader audience. Remember this is something you could see Darnell Voss, Otto Frame, and your mother holding.

Here's the great part: We are leaving all of the designing up to you!

You can redesign everything and anything you want (change colors, company logo design, content, etc.). Think of it as a blank canvas.

If you have any questions regarding design or BRISKLO Vigor, Inc. in general, please feel free to email us at design@brisk-lo.example or check out our website at www.brisk-lo.example.

Good luck!

Hi Everyone! 

Thank you to everyone who has submitted designs! Seeing what you all have come up with is exciting and impressive. However, we want to address a few commonly asked questions as well as a few general comments we have overall. 

To start, we'll better explain what we want to see in the designs. 

Although we are an energy company, we are looking to be very contemporary and sleek. Our current brand and packaging is bright and colorful, but that doesn't necessarily fit with the repositioning of our brand as a mainstream energy brand. Designs should try to only include a few colors at most. Each tablet packet should look great one their own and amazing together. 

Moreover, the designs should be relatively minimalistic. We aren't looking for anything to be "in your face". We need to reintroduce to the 18-34 generation that taking energy tablets are safe, effective, and a superior way of consuming energy supplements. Therefore, an approachable packet design is imperative. Neon colors, electricity, etc. only makes the product look scary and intimidating. 

To sum up:
Ø Use only a few colors
Ø Target an 18-34 year old demographic
Ø Minimalistic/approachable design
Ø Move away from Retro look with bright colors

FAQs:
1) We have been asked about whether or not you should be redesigning the logo on the packaging also. The answer is YES. We want every part of the packets updated. You are also designing 3 different packets or our whole energy tablet line (Surge Mix, Summit Mix, and Botanic Mix). 

2) The packets have a height of 4'' and a width of 3''. They are double-sided, so if you have a creative way of designing the back panel with the supplement facts, we would love to see it. 

We want all of you to know that we appreciate all of your hard work on creating these designs and helping to rebrand our company. Again, if you have any questions at all, the best way to reach us is by emailing us at design@brisk-lo.example. 

THANK YOU!!

The BRISKLO Design Team

Reason: We are extending the deadline for designs until Friday April 26th. We hope this will give designers a chance to submit final designs for the competition. As always, please feel free to email us directly at design@brisk-lo.example if you have any questions.

Hi everyone!

Just to let you all know, the design contest ends at 1:37am on Saturday, April 27th. We didn't want to mislead any of you by saying the contest ends tomorrow since you only have an hour and a half to submit any designs after 12am tonight. Therefore, we suggest you submit any designs you want considered by tonight. 

Thanks and good luck! 

The BRISKLO Design Team

Target Market(s)

18-34 year olds. Active, mainstream audience (not extreme-sports fans)

Requirements
Must have
• Product packet is 4''x3''
Should not have
• -Pictures of sports equipment.
-Resemble other energy products
-Look scary or intimidating
-Should not look like a cartoon or animation
-No neon colors

```html
<!DOCTYPE html>
<html lang="en">
<head>
<meta charset="utf-8">
<title>BriskLo Vigor Tablets – Packet Labels</title>
<link rel="stylesheet" href="https://fonts.googleapis.com/css2?family=Roboto+Condensed:ital,wght@0,400;0,700;0,900;1,700&display=swap">
<style>
  :root{
    --ink:#1e1e24;
    --brand-purple:#3a2a7c;
    --flame-a:#f39a3c;
    --flame-b:#e0572a;
    --white:#ffffff;
  }
  html,body{margin:0;padding:0;width:1200px;height:2600px;overflow:hidden;background:var(--white);}
  body{font-family:"Roboto Condensed",Arial,sans-serif;color:var(--ink);position:relative;}

  .packet{position:absolute;left:120px;width:960px;height:800px;overflow:hidden;
    background:linear-gradient(90deg,var(--deep) 0%,var(--mid) 40%,var(--pale) 70%,var(--pale) 100%);}
  .packet--summit{top:60px;--deep:#5e5e62;--mid:#a8a8ac;--pale:#dcdcde;--accent:#2f2f33;--tab:#e8e8ea;--tab-ink:#333338;}
  .packet--surge{top:880px;--deep:#15589c;--mid:#4f9bd8;--pale:#bcdcf3;--accent:#155ea6;--tab:#d6e8f6;--tab-ink:#15589c;}
  .packet--botanic{top:1700px;--deep:#1f7a34;--mid:#55ad55;--pale:#c3e6be;--accent:#1f7a34;--tab:#9ed34a;--tab-ink:#ffffff;}

  .front{position:absolute;left:0;top:0;width:470px;height:800px;
    background:radial-gradient(circle at 55% 45%,rgba(255,255,255,.75) 0%,rgba(255,255,255,.2) 35%,rgba(255,255,255,0) 65%);}
  .tablets-tag{position:absolute;left:22px;top:18px;font-size:15px;font-weight:700;letter-spacing:1px;color:var(--white);}
  .energy-word{position:absolute;left:318px;top:20px;font-size:42px;font-weight:700;font-style:italic;color:var(--white);letter-spacing:2px;}
  .brand-name{position:absolute;left:26px;top:90px;font-size:118px;font-weight:900;color:var(--brand-purple);line-height:1;}
  .brand-name::after{content:"";position:absolute;left:100%;top:38px;margin-left:10px;width:16px;height:16px;border-radius:50%;background:var(--brand-purple);}
  .flame-art{position:absolute;left:40px;top:250px;width:190px;height:240px;border-radius:40% 40% 20% 20%;
    background:linear-gradient(180deg,var(--flame-a),var(--flame-b));}
  .ingredient-lines{position:absolute;left:-30px;top:520px;width:360px;transform:rotate(-62deg);transform-origin:center;
    font-size:24px;font-weight:700;line-height:1.15;color:var(--white);text-align:center;}
  .ingredient-lines span{display:block;font-size:15px;font-weight:400;}
  .blend-tab{position:absolute;left:300px;top:470px;width:150px;height:330px;background:var(--tab);
    clip-path:polygon(55% 0,100% 0,100% 100%,0 100%,0 40%);}
  .blend-name{position:absolute;left:310px;top:640px;width:200px;transform:rotate(-68deg);transform-origin:center;
    font-size:40px;font-weight:900;color:var(--tab-ink);text-align:center;line-height:1;}

  .info-column{position:absolute;left:480px;top:24px;width:190px;font-size:11px;line-height:1.35;}
  .info-column p{margin:0 0 9px;}
  .icon-row{display:flex;gap:8px;margin:14px 0;}
  .icon-row i{display:block;width:30px;height:30px;background:var(--accent);}
  .fine-print{font-size:9.5px;}

  .facts-column{position:absolute;left:690px;top:20px;width:248px;font-size:11px;}
  .web-line{display:flex;align-items:center;gap:6px;font-size:10px;margin-bottom:10px;justify-content:flex-end;}
  .web-line i{display:block;width:16px;height:16px;border-radius:50%;background:var(--accent);}
  .facts-table{width:100%;border-collapse:collapse;border:2px solid var(--ink);background:rgba(255,255,255,.55);}
  .facts-table caption{font-size:20px;font-weight:900;text-align:left;padding:0 0 2px;}
  .facts-table th,.facts-table td{padding:2px 5px;border-bottom:1px solid var(--ink);text-align:left;font-weight:400;}
  .facts-table thead th{font-weight:700;border-bottom:4px solid var(--ink);}
  .facts-table td.num{text-align:right;}
  .other-ingredients{margin:12px 0 6px;line-height:1.35;}
  .approval{margin:0 0 12px;font-size:10px;}
  .cross-sell{font-size:15px;font-weight:700;font-style:italic;color:var(--accent);}
</style>
</head>
<body>

<section class="packet packet--summit" aria-label="Summit Mix packet">
  <div class="front">
    <div class="tablets-tag">TABLETS</div>
    <div class="energy-word">ENERGY</div>
    <div class="brand-name">BriskLo</div>
    <div class="flame-art" role="img" aria-label="Orange flame illustration rising beneath the brand name"></div>
    <div class="ingredient-lines">5-HTP / CHOLINE / B12<span>vitamin energy formula</span></div>
    <div class="blend-tab"></div>
    <div class="blend-name">SUMMIT MIX</div>
  </div>
  <div class="info-column">
    <p>BriskLo Summit Mix is the strongest tablet in our line, built for long days and late nights. Each tablet blends vitamins and natural ingredients for steady focus without the crash.</p>
    <p>Directions: Chew one tablet as needed. Do not exceed four tablets per day.</p>
    <p>Caution: Not for children or pregnant women. Ask a doctor before use.</p>
    <div class="icon-row"><i></i><i></i><i></i><i></i></div>
    <p class="fine-print">Distributed by BRISKLO Vigor, Inc.<br>100 Harbor Lane, Marlow Bay, CA 90000</p>
    <p class="fine-print">Made in the USA &nbsp; 6 tablets</p>
  </div>
  <div class="facts-column">
    <div class="web-line"><i></i><i></i>www.brisk-lo.example</div>
    <table class="facts-table">
      <caption>Supplement Facts</caption>
      <thead><tr><th>Serving Size 1 Tablet</th><th>%DV</th></tr></thead>
      <tbody>
        <tr><td>Vitamin C 60mg</td><td class="num">100%</td></tr>
        <tr><td>Niacin 20mg</td><td class="num">100%</td></tr>
        <tr><td>Vitamin B6 2mg</td><td class="num">100%</td></tr>
        <tr><td>Vitamin B12 6mcg</td><td class="num">100%</td></tr>
        <tr><td>5-HTP 25mg</td><td class="num">*</td></tr>
        <tr><td>Choline 50mg</td><td class="num">*</td></tr>
        <tr><td>Caffeine 100mg</td><td class="num">*</td></tr>
      </tbody>
    </table>
    <p class="other-ingredients">Other ingredients: dextrose, citric acid, natural flavor, magnesium stearate.</p>
    <p class="approval">Quality checked and approved</p>
    <p class="cross-sell">Try our BRISKLO Vigor Drinks!</p>
  </div>
</section>

<section class="packet packet--surge" aria-label="Surge Mix packet">
  <div class="front">
    <div class="tablets-tag">TABLETS</div>
    <div class="energy-word">ENERGY</div>
    <div class="brand-name">BriskLo</div>
    <div class="flame-art" role="img" aria-label="Orange flame illustration rising beneath the brand name"></div>
    <div class="ingredient-lines">CoQ10 / GINSENG / CAFFEINE<span>vitamin energy formula</span></div>
    <div class="blend-tab"></div>
    <div class="blend-name">SURGE MIX</div>
  </div>
  <div class="info-column">
    <p>BriskLo Surge Mix is the classic tablet that started it all, made for a quick lift anytime. Each tablet blends vitamins and natural ingredients for steady focus without the crash.</p>
    <p>Directions: Chew one tablet as needed. Do not exceed four tablets per day.</p>
    <p>Caution: Not for children or pregnant women. Ask a doctor before use.</p>
    <div class="icon-row"><i></i><i></i><i></i><i></i></div>
    <p class="fine-print">Distributed by BRISKLO Vigor, Inc.<br>100 Harbor Lane, Marlow Bay, CA 90000</p>
    <p class="fine-print">Made in the USA &nbsp; 6 tablets</p>
  </div>
  <div class="facts-column">
    <div class="web-line"><i></i><i></i>www.brisk-lo.example</div>
    <table class="facts-table">
      <caption>Supplement Facts</caption>
      <thead><tr><th>Serving Size 1 Tablet</th><th>%DV</th></tr></thead>
      <tbody>
        <tr><td>Vitamin C 60mg</td><td class="num">100%</td></tr>
        <tr><td>Niacin 20mg</td><td class="num">100%</td></tr>
        <tr><td>Vitamin B6 2mg</td><td class="num">100%</td></tr>
        <tr><td>Vitamin B12 6mcg</td><td class="num">100%</td></tr>
        <tr><td>CoQ10 20mg</td><td class="num">*</td></tr>
        <tr><td>Ginseng 50mg</td><td class="num">*</td></tr>
        <tr><td>Caffeine 80mg</td><td class="num">*</td></tr>
      </tbody>
    </table>
    <p class="other-ingredients">Other ingredients: dextrose, citric acid, natural flavor, magnesium stearate.</p>
    <p class="approval">Quality checked and approved</p>
    <p class="cross-sell">Try our BRISKLO Vigor Drinks!</p>
  </div>
</section>

<section class="packet packet--botanic" aria-label="Botanic Mix packet">
  <div class="front">
    <div class="tablets-tag">TABLETS</div>
    <div class="energy-word">ENERGY</div>
    <div class="brand-name">BriskLo</div>
    <div class="flame-art" role="img" aria-label="Orange flame illustration rising beneath the brand name"></div>
    <div class="ingredient-lines">GINSENG / GREEN TEA / GUARANA<span>plant energy formula</span></div>
    <div class="blend-tab"></div>
    <div class="blend-name">BOTANIC MIX</div>
  </div>
  <div class="info-column">
    <p>BriskLo Botanic Mix draws its lift from plants and herbs for a gentle, natural boost. Each tablet blends vitamins and natural ingredients for steady focus without the crash.</p>
    <p>Directions: Chew one tablet as needed. Do not exceed four tablets per day.</p>
    <p>Caution: Not for children or pregnant women. Ask a doctor before use.</p>
    <div class="icon-row"><i></i><i></i><i></i><i></i></div>
    <p class="fine-print">Distributed by BRISKLO Vigor, Inc.<br>100 Harbor Lane, Marlow Bay, CA 90000</p>
    <p class="fine-print">Made in the USA &nbsp; 6 tablets</p>
  </div>
  <div class="facts-column">
    <div class="web-line"><i></i><i></i>www.brisk-lo.example</div>
    <table class="facts-table">
      <caption>Supplement Facts</caption>
      <thead><tr><th>Serving Size 1 Tablet</th><th>%DV</th></tr></thead>
      <tbody>
        <tr><td>Vitamin C 60mg</td><td class="num">100%</td></tr>
        <tr><td>Niacin 20mg</td><td class="num">100%</td></tr>
        <tr><td>Vitamin B6 2mg</td><td class="num">100%</td></tr>
        <tr><td>Vitamin B12 6mcg</td><td class="num">100%</td></tr>
        <tr><td>Ginseng 50mg</td><td class="num">*</td></tr>
        <tr><td>Green Tea 40mg</td><td class="num">*</td></tr>
        <tr><td>Guarana 60mg</td><td class="num">*</td></tr>
      </tbody>
    </table>
    <p class="other-ingredients">Other ingredients: dextrose, citric acid, natural flavor, magnesium stearate.</p>
    <p class="approval">Quality checked and approved</p>
    <p class="cross-sell">Try our BRISKLO Vigor Drinks!</p>
  </div>
</section>

</body>
</html>
```